Business Card for a Floral & Decorating Business

I would like to take my current logo and create a better business card. I am looking for elegance as I am a florist and event decorator. My logo has multiple colour options. I like colours like green, purple, pink and orange, I think I would like a white card, open to black back ground. I want it to feel elegant and romantic. I like metallic lettering that maybe is indented in the paper, I also like glossy paper. I have a full logo already as well as a badge. I have attached both in multiple colours.m
Updates

Need extra days to review

Target Market(s)

Weddings, special events, floral customers

Industry/Entity Type

Floral and decorating

Contact Information for Business Card

Phone number, email, instagram, facebook, title, name, logo

Font styles to use
Script

Requirements
Nice to have
• Elegant

```html
<!DOCTYPE html>
<html lang="en">
<head>
<meta charset="utf-8">
<title>Wrenfield Hale – Business Card</title>
<link rel="stylesheet" href="https://fonts.googleapis.com/css2?family=Libre+Baskerville:wght@400;700&display=swap">
<style>
  :root {
    --backdrop: #2b2e34;
    --card: #ffffff;
    --plum: #7a5a8e;
    --sage: #4f8a78;
    --peach: #e3a58d;
    --faint: #eceeed;
    --serif: "Libre Baskerville", "Times New Roman", serif;
  }
  * { box-sizing: border-box; margin: 0; padding: 0; }
  html, body { width: 1200px; height: 1000px; overflow: hidden; }
  body {
    background: var(--backdrop);
    font-family: var(--serif);
    position: relative;
  }
  .card {
    position: absolute;
    left: 220px;
    width: 760px;
    height: 434px;
    background: var(--card);
    border-radius: 22px;
    overflow: hidden;
  }
  .card--front { top: 50px; }
  .card--back { top: 516px; }

  /* Front */
  .brand-mark {
    position: absolute;
    left: 60px; top: 0; width: 320px; height: 100%;
    display: flex; align-items: center; justify-content: center; gap: 14px;
  }
  .brand-mark__dot {
    width: 22px; height: 22px; border-radius: 50%;
    background: var(--plum);
  }
  .brand-mark__name {
    color: var(--plum);
    font-size: 30px;
    font-weight: 400;
  }
  .divider {
    position: absolute;
    left: 410px; top: 90px;
    width: 1.5px; height: 254px;
    background: var(--plum);
  }
  .contact {
    position: absolute;
    left: 440px; top: 118px;
    color: var(--plum);
  }
  .contact__name {
    font-size: 22px; font-weight: 700; letter-spacing: 1px;
  }
  .contact__title {
    color: var(--sage);
    font-size: 14px; letter-spacing: 1.5px;
    margin-top: 4px; margin-bottom: 14px;
  }
  .contact__row {
    display: flex; align-items: center; gap: 10px;
    font-size: 15px; line-height: 26px;
  }
  .contact__icon { width: 18px; height: 18px; flex: none; }
  .contact__address {
    font-size: 15px; line-height: 22px; margin-top: 12px;
  }

  /* Back */
  .faint-disc {
    position: absolute;
    right: 40px; top: 70px;
    width: 330px; height: 330px; border-radius: 50%;
    background: var(--faint);
  }
  .back-mark {
    position: absolute;
    left: 0; top: 0; width: 100%; height: 100%;
    display: flex; align-items: center; justify-content: center; gap: 16px;
  }
  .back-mark__dot {
    width: 26px; height: 26px; border-radius: 50%;
    background: var(--sage);
  }
  .back-mark__name {
    color: var(--sage);
    font-size: 44px;
    font-weight: 400;
    position: relative;
  }
</style>
</head>
<body>
  <section class="card card--front" aria-label="Card front">
    <div class="brand-mark">
      <span class="brand-mark__dot"></span>
      <span class="brand-mark__name">Wrenfield Hale</span>
    </div>
    <div class="divider"></div>
    <div class="contact">
      <p class="contact__name">CLARA BENTON</p>
      <p class="contact__title">MANAGING DIRECTOR</p>
      <p class="contact__row">
        <svg class="contact__icon" viewBox="0 0 20 20" aria-hidden="true">
          <circle cx="10" cy="10" r="10" fill="var(--peach)"/>
          <path d="M7 5.5l2 2-1.2 1.4a7 7 0 0 0 3.3 3.3l1.4-1.2 2 2-1.3 1.5C9.6 14.3 5.7 10.4 5.5 6.8z" fill="#fff"/>
        </svg>
        555-318-0427
      </p>
      <p class="contact__row">
        <svg class="contact__icon" viewBox="0 0 20 20" aria-hidden="true">
          <circle cx="10" cy="10" r="10" fill="var(--peach)"/>
          <rect x="5" y="6.5" width="10" height="7" fill="#fff"/>
          <path d="M5 6.5l5 4 5-4" fill="none" stroke="var(--peach)" stroke-width="1"/>
        </svg>
        clara@wrenfieldhale.com
      </p>
      <p class="contact__row">
        <svg class="contact__icon" viewBox="0 0 20 20" aria-hidden="true">
          <circle cx="10" cy="10" r="10" fill="var(--peach)"/>
          <g fill="none" stroke="#fff" stroke-width="1">
            <circle cx="10" cy="10" r="5"/>
            <ellipse cx="10" cy="10" rx="2.2" ry="5"/>
            <path d="M5 10h10M6 7.5h8M6 12.5h8"/>
          </g>
        </svg>
        www.wrenfieldhale.com
      </p>
      <p class="contact__address">410 Orchard Street NW<br>Suite 200, Millbrook<br>MI 49000</p>
    </div>
  </section>

  <section class="card card--back" aria-label="Card back">
    <div class="faint-disc"></div>
    <div class="back-mark">
      <span class="back-mark__dot"></span>
      <span class="back-mark__name">Wrenfield Hale</span>
    </div>
  </section>
</body>
</html>
```